Varubo Highlands coffee needs bold, new coffee pack design

Having just developed a new logo (see attached file), we are now in the process of developing new coffee bag packaging designs. We are using a custom bag printer in the US, so the design will need will need to follow a specific art spec/template (which has also been uploaded). We will eventually need designs for two different coffee brands/types and two different size bags (essentially a 250g and 500g size). At this point, however, our goal is to develop a design for one size/coffee brand and from there work on variations for the others.
Updates

Project Deadline Extended
Reason: We are considering some small changes to the original design we outlined and want to allow extra time for current and new designers to make those tweaks. Thanks for your consideration of our coffee package project!

Hello, After reviewing some designs so far, and receiving additional feedback from test users in our market, we are making some changes to the template design. I have uploaded a new version of the template content, which has the following changes. 1. The two side panels are now without any text, but a visual design/pattern that you want to try there is still welcome. 2. The front and bag sections has been cleaned up a bit to have less text and more room for a visual design. 3. We would like to see stronger user of the following colors: red, yellow, black (which are Ugandan flag colors) and white. Some green as needed is allowed. 4. I have uploaded a map file showing Uganda including the Varubo region where the coffee comes from. Would like to incorporate this on the back side, ideally with a small Varubo Highlands logo pointing to the region in the bottom left in green or could even say something like "Home of Varubo Highlands Coffee.". Also the country should be titled "Uganda" to make that clear. With these changes, if you need more time on the design, let me know and we can look at extending the deadline. Thank you!

Hello, Although it is not showing just yet, we expect to have a one-week extension for this contest (so not ending on 29 September, but October 6). If you are working on a design, or re-design, please continue to do so as the contest will be extended. If you are interested in starting work, please do so. Thanks for your interest in our package design contest and I look forward to seeing your work soon. Doriel

Hello, Thank you to everyone who has submitted designs so far. We want to highlight two important items at this point: 1. Based on user feedback, we are changing the design considerations bit. The size and shape of the bags are not changing, but some of the creative content is. A new file has been uploaded entitled Coffee package content 250g size v3.pdf which details these changes. Please download and read that for updates. If you have any questions, please let me know. 2. Due to these changes, we are extending this contest for another week, so I'm hopeful you will have time to make changes and submit your new ideas! Thank you, Doriel

Target Market(s)

Varubo Highlands is a premium Ugandan coffee. We are targeting those drinkers who appreciate and seek out great coffee.

Industry/Entity Type

Printer

Font styles to use
Sans Serif

Colors
ec1f27
ffffff
9bcb3c
ffcf3e

Requirements
Must have
• The attached PDF file (coffee package content) design and content elements that need to be included. Designer has strong license to determine HOW they should be designed and shown. In terms of colors, would like to see strong use of red, black, yellow (Ugandan flag colors) and white. Green is also an option if needed.

The design file will need to follow specs that are detailed here:
http://www.pelmacrate.com/artwork_specs and be in the format shown in the uploaded file 5-8 oz Bag Template.pdf.
Nice to have
• Bag should be simple, but elegant. We did testing and found that too much information was distracting so we have pared down the design/content elements to the basics. Still, creative elements or patterns and overlays are very welcome.
Should not have
• The tone should be elegant and creative, but not hokey or too handmade looking. Watch the use of too many fonts and low-contrast colors with text on background.

```html
<!DOCTYPE html>
<html lang="en">
<head>
<meta charset="utf-8">
<title>Varubo Highlands – Coffee Bag Fronts</title>
<link href="https://fonts.googleapis.com/css2?family=Archivo:ital,wght@0,400;0,600;0,700;1,700&display=swap" rel="stylesheet">
<style>
  :root {
    --canvas: #d9d9d9;
    --brand-red: #b3232a;
    --ink: #1a1a1a;
    --white: #ffffff;
    --bean: #c9a487;
    --sunset-top: #f1d6c4;
    --sunset-mid: #6f7a3a;
    --sunset-low: #2c4a1e;
    --morning-top: #f3e6d2;
    --morning-mid: #4a8a3c;
    --morning-low: #1c4a34;
    --dark-top: #dde2ea;
    --dark-mid: #5e4258;
    --dark-low: #2a2230;
    --bag-base: #0f0f0f;
  }
  * { margin: 0; padding: 0; box-sizing: border-box; }
  html, body { width: 1200px; height: 734px; overflow: hidden; }
  body {
    background: var(--canvas);
    font-family: "Archivo", Arial, sans-serif;
    position: relative;
  }
  .bag {
    position: absolute;
    top: 120px;
    width: 218px;
    height: 430px;
    overflow: hidden;
    color: var(--white);
  }
  .bag--sunset  { left: 207px; }
  .bag--morning { left: 483px; height: 468px; }
  .bag--dark    { left: 780px; }

  .bag__scene { position: absolute; inset: 0; }
  .bag--sunset .bag__scene {
    background: linear-gradient(180deg, var(--sunset-top) 0%, #f7f0ea 26%, #c7ab9e 42%, #8a6a4a 52%, var(--sunset-mid) 64%, var(--sunset-low) 84%, var(--bag-base) 100%);
  }
  .bag--morning .bag__scene {
    background: linear-gradient(180deg, var(--morning-top) 0%, #f8f3ea 26%, #c8c0a4 42%, var(--morning-mid) 62%, var(--morning-low) 84%, var(--bag-base) 100%);
  }
  .bag--dark .bag__scene {
    background: linear-gradient(180deg, var(--dark-top) 0%, #f2f3f6 26%, #b6aebd 42%, var(--dark-mid) 60%, var(--dark-low) 84%, var(--bag-base) 100%);
  }

  .brand {
    position: absolute;
    top: 62px; left: 0; right: 0;
    text-align: center;
  }
  .bag--morning .brand { top: 70px; }
  .brand__mark {
    width: 44px; height: 44px;
    margin: 0 auto 16px;
    border-radius: 50%;
    background: var(--ink);
  }
  .brand__name {
    font-weight: 700;
    font-size: 19px;
    color: var(--brand-red);
    line-height: 1;
  }
  .brand__tagline {
    margin-top: 4px;
    font-size: 5.5px;
    font-weight: 700;
    letter-spacing: 1.4px;
    color: var(--ink);
  }

  .product {
    position: absolute;
    top: 266px; left: 0; right: 0;
    text-align: center;
  }
  .bag--morning .product { top: 288px; }
  .product__name {
    font-weight: 700;
    font-style: italic;
    font-size: 15px;
    line-height: 1.1;
    text-shadow: 0 1px 2px rgba(0,0,0,.5);
  }
  .roast-scale {
    display: flex;
    justify-content: center;
    gap: 6px;
    margin-top: 4px;
  }
  .roast-scale__step { width: 20px; text-align: center; }
  .roast-scale__icon { display: block; margin: 0 auto; }
  .roast-scale__label { display: block; font-size: 5px; margin-top: 2px; white-space: nowrap; }
  .roast-scale__tick { display: block; margin: 3px auto 0; }

  .description {
    position: absolute;
    left: 0; right: 0;
    top: 355px;
    text-align: center;
    font-size: 6px;
    line-height: 1.45;
  }
  .bag--morning .description { top: 382px; }
  .weight {
    position: absolute;
    right: 16px; bottom: 28px;
    font-size: 7px;
    color: var(--white);
  }
  .bag--morning .weight { bottom: 34px; right: 31px; }
</style>
</head>
<body>

<svg width="0" height="0" style="position:absolute">
  <defs>
    <symbol id="roast-icon" viewBox="0 0 12 12">
      <circle cx="6" cy="6" r="5.3" fill="#c9a487" stroke="#fff" stroke-width="0.8"/>
      <line x1="3.5" y1="8.5" x2="8.5" y2="3.5" stroke="#5a3a26" stroke-width="1"/>
    </symbol>
    <symbol id="tick" viewBox="0 0 10 8">
      <polyline points="1,4 4,7 9,1" fill="none" stroke="#fff" stroke-width="1.2"/>
    </symbol>
  </defs>
</svg>

<article class="bag bag--sunset">
  <div class="bag__scene" role="img" aria-label="Misty terraced highland coffee fields at sunset"></div>
  <header class="brand">
    <div class="brand__mark"></div>
    <div class="brand__name">Varubo Highlands</div>
    <div class="brand__tagline">PREMIUM UGANDAN COFFEE</div>
  </header>
  <section class="product">
    <h2 class="product__name">Sunset Roast</h2>
    <div class="roast-scale">
      <div class="roast-scale__step"><svg class="roast-scale__icon" width="12" height="12"><use href="#roast-icon"/></svg><span class="roast-scale__label">Light</span></div>
      <div class="roast-scale__step"><svg class="roast-scale__icon" width="12" height="12"><use href="#roast-icon"/></svg><span class="roast-scale__label">Medium</span><svg class="roast-scale__tick" width="9" height="7"><use href="#tick"/></svg></div>
      <div class="roast-scale__step"><svg class="roast-scale__icon" width="12" height="12"><use href="#roast-icon"/></svg><span class="roast-scale__label">Dark</span></div>
      <div class="roast-scale__step"><svg class="roast-scale__icon" width="12" height="12"><use href="#roast-icon"/></svg><span class="roast-scale__label">Very Dark</span></div>
    </div>
  </section>
  <p class="description">A bold, rich Arabica dark roast<br>with hints of vanilla and almond.</p>
  <p class="weight">250g | 9oz</p>
</article>

<article class="bag bag--morning">
  <div class="bag__scene" role="img" aria-label="Misty terraced green highland coffee fields in morning light"></div>
  <header class="brand">
    <div class="brand__mark"></div>
    <div class="brand__name">Varubo Highlands</div>
    <div class="brand__tagline">PREMIUM UGANDAN COFFEE</div>
  </header>
  <section class="product">
    <h2 class="product__name">Morning Roast</h2>
    <div class="roast-scale">
      <div class="roast-scale__step"><svg class="roast-scale__icon" width="12" height="12"><use href="#roast-icon"/></svg><span class="roast-scale__label">Light</span><svg class="roast-scale__tick" width="9" height="7"><use href="#tick"/></svg></div>
      <div class="roast-scale__step"><svg class="roast-scale__icon" width="12" height="12"><use href="#roast-icon"/></svg><span class="roast-scale__label">Medium</span></div>
      <div class="roast-scale__step"><svg class="roast-scale__icon" width="12" height="12"><use href="#roast-icon"/></svg><span class="roast-scale__label">Dark</span></div>
      <div class="roast-scale__step"><svg class="roast-scale__icon" width="12" height="12"><use href="#roast-icon"/></svg><span class="roast-scale__label">Very Dark</span></div>
    </div>
  </section>
  <p class="description">A bold, rich Arabica dark roast<br>with hints of vanilla and almond.</p>
  <p class="weight">250g | 9oz</p>
</article>

<article class="bag bag--dark">
  <div class="bag__scene" role="img" aria-label="Misty terraced highland coffee fields in dusky purple tones"></div>
  <header class="brand">
    <div class="brand__mark"></div>
    <div class="brand__name">Varubo Highlands</div>
    <div class="brand__tagline">PREMIUM UGANDAN COFFEE</div>
  </header>
  <section class="product">
    <h2 class="product__name">Dark Roast</h2>
    <div class="roast-scale">
      <div class="roast-scale__step"><svg class="roast-scale__icon" width="12" height="12"><use href="#roast-icon"/></svg><span class="roast-scale__label">Light</span></div>
      <div class="roast-scale__step"><svg class="roast-scale__icon" width="12" height="12"><use href="#roast-icon"/></svg><span class="roast-scale__label">Medium</span></div>
      <div class="roast-scale__step"><svg class="roast-scale__icon" width="12" height="12"><use href="#roast-icon"/></svg><span class="roast-scale__label">Dark</span><svg class="roast-scale__tick" width="9" height="7"><use href="#tick"/></svg></div>
      <div class="roast-scale__step"><svg class="roast-scale__icon" width="12" height="12"><use href="#roast-icon"/></svg><span class="roast-scale__label">Very Dark</span></div>
    </div>
  </section>
  <p class="description">A bold, rich Arabica dark roast<br>with hints of vanilla and almond.</p>
  <p class="weight">250g | 9oz</p>
</article>

</body>
</html>
```